Modern Fun Bold Laundry stain remover wipes and spray

Marlo Basics packaging is bold, modern, and unapologetically real—just like the messes it’s made to handle.
please look at brand guidelines for colours and text etc. Please also just use sample text where descriptions etc need to go on packaging and i will fill in later.
3 die lines. 1 a box that will contain wipes - one the wipe packet and another is just sticker that will go on stain remover spray bottle

The design is clean but not precious. High contrast colors, strong typography, and plenty of breathing room give it a confident, fast-acting feel. The look says effective first, aesthetic second—but still looks damn good on a shelf or in a laundry room.

Typography is strong, modern, and slightly irreverent. Large, clear headlines deliver attitude up front, while short punchy lines replace traditional cleaning jargon. No scripts, no frills—just bold sans-serif type that feels sharp, capable, and honest.

Copy is conversational and fearless:

Speaks directly to the customer

Acknowledges real messes (stains, spills, toilets)

Never sugarcoats or over-explains

Confident without being aggressive

Funny without trying too hard

Visual elements are minimal but intentional—simple icons, soapy suds, bubbles, subtle texture, laundry tile feel or graphic blocks that hint at motion and speed. Nothing fussy. Nothing “clinical.” This is modern utility with personality.

The overall tone:

Fun but tough

Edgy but trustworthy

Modern without being cold

Relatable without being messy

Marlo doesn’t promise perfection—she promises results.

Shelf presence: bold, eye-catching, and instantly legible from a distance.
In-hand feel: sturdy, practical, and premium without being precious.
Brand energy: “I’ve got this.”

Get it dirty. Marlo will clean it.

logo, die lines and all ideas i like are uploaded

Target Market(s)

28-48 women

Industry/Entity Type

laundry cleaning

Font styles to use
Other font styles liked:
• all fonts and colours are in brand guidelines

Requirements
Must have
• Die line box - Front - Logo, Stain remover, Fast and effective, for clothes fabric and on the go messes, 25 wipes inside. Sides - ecofriendly, fast and effective, no harsh chemicals, Vegan, travel friendly, other side a fun tagline. Back. please just put sample text I will put proper text in
Should not have
• be boring an original

```html
<!DOCTYPE html>
<html lang="en">
<head>
<meta charset="utf-8">
<title>Marlo Basics – Stain Remover Wipes Box</title>
<link rel="stylesheet" href="https://fonts.googleapis.com/css2?family=Montserrat:wght@400;600;800&display=swap">
<style>
  :root {
    --page: #ffffff;
    --periwinkle: #7f8cf2;
    --periwinkle-light: #9aa6f6;
    --pink: #f08ae2;
    --pink-light: #f6a9ec;
    --white: #ffffff;
    --cut-line: #6f7bd8;
  }
  * { box-sizing: border-box; margin: 0; padding: 0; }
  html, body { width: 793px; height: 1200px; overflow: hidden; background: var(--page); }
  body { font-family: "Montserrat", sans-serif; color: var(--white); }
  .canvas { position: relative; width: 793px; height: 1200px; }

  /* Flat box view */
  .panel { position: absolute; overflow: hidden; }
  .box-front { left: 117px; top: 60px; width: 370px; height: 320px; background: var(--periwinkle); }
  .box-side { left: 487px; top: 60px; width: 190px; height: 320px; background: var(--pink); }

  .bubble { position: absolute; border-radius: 50%; }
  .bubble--blue { background: var(--periwinkle-light); opacity: .55; }
  .bubble--pink { background: var(--pink-light); opacity: .6; }

  .product-line {
    position: absolute; left: 0; right: 0;
    text-align: center; font-weight: 400; letter-spacing: .18em;
    text-transform: lowercase;
  }
  .logo-seal {
    position: absolute; border: 3px solid var(--white); border-radius: 50%;
    display: flex; align-items: center; justify-content: center;
  }
  .logo-name { font-weight: 800; color: var(--white); text-align: center; line-height: 1.05; }
  .tagline { position: absolute; left: 0; right: 0; text-align: center; font-weight: 800; }

  .wordmark-vertical {
    position: absolute; top: 50%; left: 50%;
    transform: translate(-50%, -50%) rotate(-90deg);
    text-align: center; white-space: nowrap;
  }
  .wordmark-vertical .brand { display: block; font-weight: 800; line-height: 1; }
  .wordmark-vertical .sub { display: block; font-weight: 400; letter-spacing: .2em; }

  /* Dieline */
  .dieline { position: absolute; left: 0; top: 0; }
  .overlay { position: absolute; }
  .upside-down { transform: rotate(180deg); text-align: center; }
</style>
</head>
<body>
<main class="canvas">

  <!-- Flat front panel -->
  <section class="panel box-front">
    <span class="bubble bubble--blue" style="left:-60px;top:170px;width:200px;height:200px"></span>
    <span class="bubble bubble--blue" style="left:250px;top:-50px;width:160px;height:160px"></span>
    <span class="bubble bubble--blue" style="left:290px;top:230px;width:110px;height:110px"></span>
    <p class="product-line" style="top:36px;font-size:17px">stain remover wipes</p>
    <div class="logo-seal" style="left:100px;top:80px;width:170px;height:170px">
      <span class="logo-name" style="font-size:28px">Marlo<br>Basics</span>
    </div>
    <p class="tagline" style="top:272px;font-size:16px">Get it dirty. Marlo will clean it.</p>
  </section>

  <!-- Flat side panel -->
  <section class="panel box-side">
    <span class="bubble bubble--pink" style="left:-50px;top:-40px;width:150px;height:150px"></span>
    <span class="bubble bubble--pink" style="left:100px;top:220px;width:140px;height:140px"></span>
    <div class="wordmark-vertical">
      <span class="brand" style="font-size:64px">Marlo</span>
      <span class="sub" style="font-size:12px">stain remover wipes</span>
    </div>
  </section>

  <!-- Dieline shapes -->
  <svg class="dieline" width="793" height="1200" viewBox="0 0 793 1200" aria-hidden="true">
    <defs>
      <clipPath id="clip-left"><path d="M8 860 H40 V840 H259 V1163 H230 V1190 H180 V1163 H90 V1190 H40 V1163 H8 Z"/></clipPath>
      <clipPath id="clip-pink-a"><path d="M259 840 H290 V788 H395 V840 H418 V1163 H259 Z"/></clipPath>
      <clipPath id="clip-center"><path d="M418 846 V670 Q418 655 433 655 H572 Q587 655 587 670 V846 V1163 H560 L545 1190 H460 L445 1163 H418 Z"/></clipPath>
      <clipPath id="clip-pink-b"><path d="M587 840 H610 V788 H700 V840 H722 V1136 H587 Z"/></clipPath>
    </defs>

    <g clip-path="url(#clip-left)">
      <rect x="0" y="780" width="270" height="420" fill="var(--periwinkle)"/>
      <circle cx="40" cy="1110" r="80" fill="var(--periwinkle-light)" opacity=".55"/>
      <circle cx="230" cy="880" r="60" fill="var(--periwinkle-light)" opacity=".55"/>
    </g>
    <g clip-path="url(#clip-pink-a)">
      <rect x="255" y="780" width="170" height="400" fill="var(--pink)"/>
      <circle cx="270" cy="830" r="60" fill="var(--pink-light)" opacity=".6"/>
      <circle cx="410" cy="1120" r="60" fill="var(--pink-light)" opacity=".6"/>
    </g>
    <g clip-path="url(#clip-center)">
      <rect x="410" y="650" width="185" height="550" fill="var(--periwinkle)"/>
      <circle cx="430" cy="1100" r="70" fill="var(--periwinkle-light)" opacity=".55"/>
      <circle cx="580" cy="880" r="55" fill="var(--periwinkle-light)" opacity=".55"/>
    </g>
    <g clip-path="url(#clip-pink-b)">
      <rect x="580" y="780" width="150" height="370" fill="var(--pink)"/>
      <circle cx="600" cy="820" r="55" fill="var(--pink-light)" opacity=".6"/>
      <circle cx="720" cy="1090" r="55" fill="var(--pink-light)" opacity=".6"/>
    </g>
    <line x1="418" y1="846" x2="587" y2="846" stroke="var(--cut-line)" stroke-width="1" opacity=".6"/>
  </svg>

  <!-- Dieline: left front panel -->
  <div class="overlay logo-seal" style="left:68px;top:925px;width:130px;height:130px">
    <span class="logo-name" style="font-size:21px">Marlo<br>Basics</span>
  </div>

  <!-- Dieline: first pink side -->
  <div class="overlay" style="left:259px;top:840px;width:159px;height:323px">
    <div class="wordmark-vertical">
      <span class="brand" style="font-size:56px">Marlo</span>
      <span class="sub" style="font-size:10px">stain remover wipes</span>
    </div>
  </div>

  <!-- Dieline: center top flap (upside down) -->
  <div class="overlay upside-down" style="left:418px;top:700px;width:169px">
    <p style="font-weight:800;font-size:44px;line-height:1">Marlo</p>
    <p style="font-size:10px;letter-spacing:.2em">stain remover wipes</p>
  </div>

  <!-- Dieline: center front panel -->
  <div class="overlay logo-seal" style="left:447px;top:905px;width:112px;height:112px">
    <span class="logo-name" style="font-size:18px">Marlo<br>Basics</span>
  </div>
  <p class="overlay tagline" style="left:418px;right:auto;width:169px;top:1045px;font-size:10.5px">Get it dirty. Marlo will clean it.</p>

  <!-- Dieline: second pink side -->
  <div class="overlay" style="left:587px;top:840px;width:135px;height:296px">
    <div class="wordmark-vertical">
      <span class="brand" style="font-size:50px">Marlo</span>
      <span class="sub" style="font-size:9px">stain remover wipes</span>
    </div>
  </div>

</main>
</body>
</html>
```